Brochure Cover and Back pages

We are a US-based cosmetics company that sells state-of-the-art skin care products, including advanced anti-aging serums, natural mineral sunscreens, organic antioxidant moisturizers, and organic face cleansers. We need a product brochure. We already have chosen a design for the layout of the product info pages. But we still need a cover page and a back page. We are looking for simple but elegant design for the cover page. The back page is less important and we already know what we want on the back page. It will be the company's mission statement and at the bottom, the company URL, phone number, etc.

The brochure has two folds. So there will be three panels on both sides. The size of each panel is 16.5 (l) x 9.5 (w) cm.

At the end of the project, we expect the designer to integrate all the pages so that the finished copy is read to be sent off to a printing service for printing.

All the product info pages are attached. Also attached are the text (info) to go on the back page, company logo with and without the tagline, the icon in the logo.

YOu are welcome to visit our website www.morvask.com to learn about our products.

Industry/Entity Type

Cosmetics

```html
<!DOCTYPE html>
<html lang="en">
<head>
<meta charset="utf-8">
<title>Morvask Brochure – Outside Spread</title>
<link rel="stylesheet" href="https://fonts.googleapis.com/css2?family=Cinzel:wght@400;600&family=Parisienne&family=PT+Sans:wght@400;700&family=Roboto+Condensed:wght@700&display=swap">
<style>
  :root {
    --page-bg: #e4e4e4;
    --paper: #ffffff;
    --ink: #1a1a1a;
    --heading-blue: #1f5aa6;
    --band-grey: #e6e8ea;
    --silver-light: #f4f4f5;
    --silver-dark: #a9abae;
    --silk-light: #f3efe6;
    --silk-mid: #ddd5c4;
    --silk-dark: #b9ae98;
    --rose: #c0406e;
    --rose-soft: #e9b7c4;
    --logo-box: #d98f9f;
    --line-pink: #e0457e;
    --line-blue: #2952a3;
    --line-orange: #f08a24;
    --line-green: #6cbf3b;
    --orange: #f0892a;
    --orange-light: #f8b462;
  }
  * { box-sizing: border-box; margin: 0; padding: 0; }
  html, body { width: 1200px; height: 982px; overflow: hidden; }
  body { background: var(--page-bg); font-family: "PT Sans", sans-serif; color: var(--ink); }

  .spread {
    position: absolute; left: 45px; top: 170px;
    width: 1110px; height: 643px;
    display: flex;
    box-shadow: 0 6px 22px rgba(0,0,0,.22);
  }
  .panel { position: relative; width: 370px; height: 643px; overflow: hidden; }

  /* ---------- Inside flap: cleansers ---------- */
  .panel--products { background: var(--paper); }
  .products__title {
    position: absolute; top: 28px; right: 30px; text-align: left;
    font-family: "Roboto Condensed", sans-serif; font-weight: 700;
    font-size: 20px; color: var(--heading-blue); line-height: 1;
  }
  .products__subtitle {
    display: block; font-family: "PT Sans", sans-serif; font-weight: 400;
    font-size: 12px; margin-top: 3px;
  }
  .product { position: absolute; left: 0; width: 370px; height: 130px; }
  .product--shaded { background: var(--band-grey); }
  .product__text { position: absolute; left: 60px; top: 18px; width: 190px; }
  .product__name { font-weight: 700; font-size: 13px; margin-bottom: 6px; }
  .product__desc { font-size: 10.5px; line-height: 1.35; }
  .product__photo {
    position: absolute; left: 270px; top: 16px; width: 50px; height: 100px;
    border-radius: 6px 6px 3px 3px;
    background: linear-gradient(90deg, #e9eef4, #ffffff 45%, #d9e2ec);
    border-bottom: 14px solid #5b8fcf;
  }
  .products__contact {
    position: absolute; bottom: 40px; left: 60px; font-size: 14px;
  }

  /* ---------- Shared silk panels ---------- */
  .silk {
    position: absolute; inset: 0;
    background:
      radial-gradient(ellipse 60% 90% at 30% 40%, var(--silk-light), transparent 70%),
      linear-gradient(115deg, var(--silk-mid), var(--silk-light) 35%, var(--silk-dark) 55%, var(--silk-light) 75%, var(--silk-mid));
  }
  .silver-band {
    position: absolute; left: 0; width: 100%;
    background: linear-gradient(180deg, var(--silver-light), #d9dadc 50%, var(--silver-dark));
    display: flex; align-items: center; justify-content: center;
  }
  .silver-band--top { top: 0; height: 30px; }
  .silver-band--bottom { bottom: 0; height: 42px; }
  .site-url {
    font-family: "Cinzel", serif; font-size: 12px; color: var(--rose); letter-spacing: .5px;
  }

  /* ---------- Back panel ---------- */
  .back__brand {
    position: absolute; top: 385px; right: 40px;
    font-family: "Cinzel", serif; font-weight: 600; font-size: 32px; color: var(--ink);
  }
  .back__ribbon {
    position: absolute; top: 440px; left: 0; width: 100%; height: 22px;
    background: linear-gradient(90deg, transparent, var(--rose-soft) 20%, #f2cdd6);
    font-family: "Cinzel", serif; font-size: 11.5px; color: var(--rose);
    display: flex; align-items: center; justify-content: flex-end; padding-right: 22px;
  }
  .back__service {
    position: absolute; top: 474px; right: 40px; text-align: right;
    font-family: "Cinzel", serif; font-size: 11.5px; line-height: 1.45;
  }

  /* ---------- Cover panel ---------- */
  .cover__tagline {
    font-family: "Parisienne", cursive; font-size: 19px; color: var(--rose);
  }
  .cover__logo-box {
    position: absolute; top: 52px; right: 28px; width: 150px; height: 82px;
    background: var(--logo-box); border-radius: 6px;
    box-shadow: 0 2px 5px rgba(0,0,0,.25);
    display: flex; align-items: center; justify-content: center;
    font-family: "Cinzel", serif; font-weight: 600; font-size: 28px; color: var(--ink);
  }
  .categories { position: absolute; top: 220px; right: 20px; list-style: none; text-align: center; }
  .categories__item {
    font-family: "Cinzel", serif; font-size: 15px; line-height: 1.1;
    padding-bottom: 3px; margin-bottom: 4px; border-bottom: 2.5px solid;
  }
  .categories__item--serums { border-color: var(--line-pink); margin-left: 80px; }
  .categories__item--cleansers { border-color: var(--line-blue); margin-left: 50px; }
  .categories__item--sunscreens { border-color: var(--line-orange); margin-left: 25px; }
  .categories__item--moisturizers { border-color: var(--line-green); }
  .cover__photo {
    position: absolute; top: 420px; left: 60px; width: 230px; height: 170px;
    border-radius: 40% 45% 30% 30%;
    background: radial-gradient(ellipse at 45% 40%, var(--orange-light), var(--orange) 60%, rgba(240,137,42,0) 100%);
  }
</style>
</head>
<body>
  <main class="spread">
    <section class="panel panel--products">
      <h2 class="products__title">Organic Face Cleansers<span class="products__subtitle">Gentle for All Skin Types</span></h2>

      <article class="product" style="top:80px">
        <div class="product__text">
          <h3 class="product__name">Refreshing Natural Cleanser</h3>
          <p class="product__desc">This refreshing aloe-based gel cleanser is formulated with organic ingredients. It cleans thoroughly without drying out the skin. Balances skin hydration and sebum. 4 fl. oz.</p>
        </div>
        <div class="product__photo" role="img" aria-label="Cleanser tube product photo"></div>
      </article>

      <article class="product product--shaded" style="top:215px">
        <div class="product__text">
          <h3 class="product__name">Hydrating Organic Cleanser</h3>
          <p class="product__desc">This light gel cleanser is formulated with coconut milk and honey for a moisturizing wash. Gently washes away dirt and oil, leaving skin hydrated and softened. 4 fl. oz.</p>
        </div>
        <div class="product__photo" role="img" aria-label="Cleanser tube product photo"></div>
      </article>

      <article class="product" style="top:350px">
        <div class="product__text">
          <h3 class="product__name">Nourishing Cleansing Milk</h3>
          <p class="product__desc">This comforting organic lotion cleanser is enriched with botanical extracts to leave skin feeling smooth and soft. Can be used to remove eye makeup. 4 fl. oz.</p>
        </div>
        <div class="product__photo" role="img" aria-label="Cleansing milk tube product photo"></div>
      </article>

      <p class="products__contact">www.Morvask.com &nbsp;1-855-5-Morvask</p>
    </section>

    <section class="panel panel--back">
      <div class="silk" role="img" aria-label="Draped cream silk fabric background"></div>
      <div class="silver-band silver-band--top"></div>
      <p class="back__brand">Morvask</p>
      <p class="back__ribbon">Creating Beauty Solutions Through Science</p>
      <address class="back__service" style="font-style:normal">
        Customer Service:<br>
        1-855-5-Morvask (855-566-7827)<br>
        2150 Alder Crest Rd. Suite 400<br>
        Fairview, CA 94541
      </address>
      <div class="silver-band silver-band--bottom"><span class="site-url">www.morvask.com</span></div>
    </section>

    <section class="panel panel--cover">
      <div class="silk" role="img" aria-label="Draped cream silk fabric background"></div>
      <div class="silver-band silver-band--top"><span class="cover__tagline">Bringing You Smart Skin Care</span></div>
      <div class="cover__logo-box">Morvask</div>
      <ul class="categories">
        <li class="categories__item categories__item--serums">Anti-Aging Serums</li>
        <li class="categories__item categories__item--cleansers">Organic Face Cleansers</li>
        <li class="categories__item categories__item--sunscreens">Natural Mineral Sunscreens</li>
        <li class="categories__item categories__item--moisturizers">Organic Antioxidant Moisturizers</li>
      </ul>
      <div class="cover__photo" role="img" aria-label="Halved orange with spiral-cut peel and its reflection"></div>
      <div class="silver-band silver-band--bottom"><span class="site-url">www.morvask.com</span></div>
    </section>
  </main>
</body>
</html>
```